LANTERNHILL Pizza and Wraps

We need a website for a new restaurant called LANTERNHILL "PIZZA AND WRAPS".
I have attached fonts, background images, logo, images, content etc.
can provide you with what you need to get the website design done fast and easy
Updates

I have uploaded more images of the venue and some menu items. let me know if there is anything I need to provide to make your mission clear and easy

Reason: i would like a little time to provide more feedback to designers

Industry/Entity Type

Restaurant

Coding

Coded - Design and coding required

Number of Pages Required

5+ page

Colors

Designer to choose colors to be used in the design.

Requirements
Must have
• PAGES:
• Our Story
• Menu
• Reservations
• Catering & Delivery
• Contact

```html
<!DOCTYPE html>
<html lang="en">
<head>
<meta charset="utf-8">
<title>LANTERNHILL Pizza and Wraps</title>
<link rel="stylesheet" href="https://fonts.googleapis.com/css2?family=Kaushan+Script&family=Julius+Sans+One&family=Raleway:wght@400;600;700&display=swap">
<style>
:root{
  --red:#e3232c;
  --red-dark:#b9151d;
  --navy:#141d33;
  --navy-wood:#24324b;
  --night:#0d1120;
  --yellow:#f5c518;
  --white:#ffffff;
  --paper:#f6f6f6;
  --ink:#222222;
  --muted:#666666;
}
*{margin:0;padding:0;box-sizing:border-box}
html,body{width:1200px;height:4383px;overflow:hidden}
body{position:relative;background:var(--white);font-family:'Raleway',sans-serif;color:var(--ink)}
.abs{position:absolute}
.script{font-family:'Kaushan Script',cursive}
.wide{font-family:'Julius Sans One',sans-serif;letter-spacing:6px;text-transform:uppercase}
.btn{display:inline-block;background:var(--red);color:var(--white);font-size:13px;font-weight:700;letter-spacing:1px;padding:10px 22px;text-transform:uppercase}

/* hero */
.hero{left:0;top:0;width:1200px;height:700px;background:linear-gradient(160deg,var(--navy-wood),#1a2538 55%,#22304a);clip-path:polygon(0 0,100% 0,100% 88%,0 100%)}
.hero-veg-left{left:-40px;top:230px;width:330px;height:330px;border-radius:50%;background:radial-gradient(circle at 45% 45%,#d8d2c2 0 38%,#7aa23a 45%,#c8402a 60%,#2e3a28 75%,transparent 76%)}
.hero-veg-right{left:900px;top:0;width:300px;height:250px;border-radius:0 0 0 60%;background:radial-gradient(circle at 60% 40%,#c52a22 0 25%,#5c8f2c 45%,#2a3a26 70%,transparent 72%)}
.hero-onion{left:880px;top:520px;width:250px;height:160px;border-radius:50%;background:radial-gradient(circle at 50% 50%,#c88a4a,#8a4d25 60%,transparent 62%)}
.logo{left:33px;top:22px;color:var(--red);font-weight:700;line-height:1}
.logo .name{font-size:34px;letter-spacing:1px}
.logo .sub{font-size:13px;letter-spacing:3px;margin-top:6px;text-transform:uppercase}
.nav{left:583px;top:26px;display:flex;gap:26px;font-size:12px;font-weight:600;color:var(--white);text-transform:uppercase;letter-spacing:1px;white-space:nowrap}
.nav .active{color:var(--red);border-bottom:2px solid var(--red);padding-bottom:4px}
.hero-title{left:0;top:235px;width:1200px;text-align:center;color:var(--white);font-size:78px;font-weight:400}
.hero-btn{left:543px;top:356px}

/* story */
.story-card{left:229px;top:717px;width:221px;height:390px;background:var(--white);box-shadow:0 4px 18px rgba(0,0,0,.15);padding:40px 26px;text-align:center}
.story-card .script{color:var(--red);font-size:40px;line-height:1}
.story-card .wide{font-size:20px;letter-spacing:4px;margin-top:6px}
.story-card p{font-size:13px;line-height:1.6;color:var(--muted);margin-top:22px}
.story-card .btn{margin-top:68px}
.story-photo-a{left:479px;top:679px;width:229px;height:396px;background:linear-gradient(180deg,#6b3a22,#b98a5a 45%,#2a1a12)}
.story-photo-b{left:729px;top:717px;width:229px;height:358px;border-radius:10px;background:radial-gradient(circle at 50% 30%,#f4c47a,#8a5a2e 45%,#2c1c12 85%)}

/* services */
.services{left:0;top:1180px;width:1200px;height:510px;background:linear-gradient(120deg,var(--night),var(--navy) 50%,#0b0f1c);clip-path:polygon(0 8%,100% 0,100% 92%,0 100%)}
.services-title{left:0;top:1240px;width:1200px;text-align:center}
.services-title .script{color:var(--yellow);font-size:42px;display:block;line-height:1}
.services-title .wide{color:var(--white);font-size:24px;display:block;margin-top:6px}
.service{top:1395px;width:237px;text-align:center}
.service .photo{height:148px;border:3px solid var(--white)}
.service .label{color:var(--white);font-family:'Julius Sans One',sans-serif;font-size:22px;letter-spacing:4px;margin-top:30px;text-transform:uppercase}

/* special menu */
.menu-title{left:0;top:1782px;width:1200px;text-align:center;color:var(--red);font-size:30px;font-weight:400}
.menu-intro{left:237px;top:1858px;width:360px;height:549px;background:var(--red);color:var(--white);padding:36px 32px;font-size:14px;line-height:1.75;text-align:center}
.menu-intro p+p{margin-top:16px}
.tile{width:180px;height:183px}
.dish-card{background:var(--white);box-shadow:0 2px 10px rgba(0,0,0,.12);text-align:center;padding-top:30px}
.dish-card .dot{width:34px;height:34px;border-radius:50%;background:var(--red);margin:0 auto}
.dish-card .script{color:var(--yellow);font-size:30px;display:block;margin-top:8px}
.dish-card small{display:block;font-size:11px;color:var(--muted);margin-top:4px}

/* events */
.events{left:0;top:2650px;width:1200px;height:700px;background:radial-gradient(circle at 30% 40%,#3d2a22,#1a1a1a 55%,#0e0e0e);clip-path:polygon(0 0,100% 8%,100% 100%,0 92%)}
.events-title{left:0;top:2752px;width:1200px;text-align:center}
.events-title .script{color:var(--yellow);font-size:46px}
.events-title .and{color:var(--white);font-size:22px}
.events-title .wide{display:block;color:var(--white);font-size:36px;margin-top:2px}
.events-text{left:229px;top:2900px;width:390px;color:var(--white);font-size:13px;line-height:1.75}
.events-text p+p{margin-top:14px}
.events-photo{left:640px;top:2880px;width:195px;height:185px;background:linear-gradient(160deg,#c0392b,#6e2a1e 50%,#d7a05a)}

/* offer cards */
.offer{top:3440px;width:292px;height:185px;background:var(--white);box-shadow:0 3px 14px rgba(0,0,0,.14);text-align:center;padding-top:28px}
.offer h3{font-family:'Julius Sans One',sans-serif;color:var(--red);font-size:24px;letter-spacing:4px;font-weight:400}
.offer p{font-size:12px;line-height:1.6;color:var(--muted);margin:16px 32px 0}
.offer-photo{left:521px;top:3440px;width:167px;height:185px;background:radial-gradient(circle at 50% 50%,#e8c58a,#7a5a3a 55%,#2a2622)}

/* reservation */
.res-title{left:0;top:3642px;width:1200px;text-align:center}
.res-title .script{color:var(--red);font-size:36px;display:block;line-height:1}
.res-title .wide{font-size:20px;display:block;margin-top:4px}
.res-band{left:0;top:3728px;width:1200px;height:262px;background:var(--red)}
.field{top:3775px;height:58px;background:var(--navy);color:var(--white);display:flex;align-items:center;gap:12px;padding:0 18px;font-size:15px;font-weight:600;white-space:nowrap}
.field svg{flex:none}
.find{left:771px;top:3775px;width:187px;height:58px;background:var(--navy);color:var(--white);font-size:14px;font-weight:700;letter-spacing:1px;display:flex;align-items:center;justify-content:center;text-transform:uppercase}
.res-note{left:208px;top:3870px;width:750px;color:var(--white);font-size:12px;line-height:1.7}

/* footer */
.footer{left:0;top:4000px;width:1200px;height:383px;background:var(--night)}
.foot-col{top:4100px;width:170px;color:#cfd3dc;font-size:12px;line-height:2}
.foot-col h4{display:inline-block;background:var(--red);color:var(--white);font-size:12px;letter-spacing:1px;padding:4px 10px;margin-bottom:14px;text-transform:uppercase}
.social{display:flex;gap:10px;margin-top:4px}
.social span{width:26px;height:26px;border-radius:50%;background:var(--red)}
.input{height:30px;border:1px solid #cfd3dc;color:#8a90a0;font-size:11px;padding:0 10px;display:flex;align-items:center;margin-bottom:10px}
.foot-photo{left:930px;top:4104px;width:270px;height:279px;background:linear-gradient(150deg,#e7d9c0,#c98b4a 40%,#b3202a 75%,#7a1218)}
</style>
</head>
<body>

<section class="hero abs"></section>
<div class="hero-veg-left abs" role="img" aria-label="Bowl of fresh salad vegetables on a wooden table"></div>
<div class="hero-veg-right abs" role="img" aria-label="Tomatoes and green herbs"></div>
<div class="hero-onion abs" role="img" aria-label="Red onions"></div>
<div class="logo abs"><div class="name">LANTERNHILL</div><div class="sub">Pizza and Wraps</div></div>
<nav class="nav abs"><span class="active">Home</span><span>Our Story</span><span>Menu</span><span>Reservation</span><span>Catering &amp; Delivery</span><span>Contact</span></nav>
<h1 class="hero-title abs script">Chase the flavors</h1>
<a class="hero-btn abs btn">Book Table</a>

<article class="story-card abs">
  <div class="script">Discover</div>
  <div class="wide">Our Story</div>
  <p>Rich in heritage, Lanternhill is a gathering place celebrating the Mediterranean's finest produce.</p>
  <a class="btn">Learn More</a>
</article>
<div class="story-photo-a abs" role="img" aria-label="Restaurant interior with brick wall and warm wood"></div>
<div class="story-photo-b abs" role="img" aria-label="Dining room with pendant lights"></div>

<section class="services abs"></section>
<div class="services-title abs"><span class="script">Specialties</span><span class="wide">Our Services</span></div>
<div class="service abs" style="left:229px"><div class="photo" role="img" aria-label="Breakfast plate with eggs" style="background:radial-gradient(circle at 50% 50%,#f0e0b0,#c0532a 50%,#3a2218)"></div><div class="label">Breakfast</div></div>
<div class="service abs" style="left:483px"><div class="photo" role="img" aria-label="Lunch bowls of salad" style="background:radial-gradient(circle at 50% 50%,#e9e1c9,#6a9a3a 50%,#2a2a22)"></div><div class="label">Lunch</div></div>
<div class="service abs" style="left:737px"><div class="photo" role="img" aria-label="Dinner plate of grilled vegetables" style="background:radial-gradient(circle at 50% 50%,#f2c44a,#b8402a 50%,#26301e)"></div><div class="label">Dinner</div></div>

<h2 class="menu-title abs wide">Special Menu</h2>
<div class="menu-intro abs">
  <p>Quality food is devotion to seasonal, finest ingredients, and meticulous care in bringing it to life on the plate. At Lanternhill, we pair a warm welcome with a relaxed setting. Choose from our dishes, made from scratch and hand rolled selection of pizzas and wraps, then sit back and let us bring it to your table.</p>
  <p>Our Mediterranean focus is further complemented by a considered variety of beverages and desserts to satisfy every taste.</p>
  <p>Discover Mediterranean tastes &amp; crafted beverages</p>
</div>
<div class="tile dish-card abs" style="left:597px;top:1858px"><div class="dot"></div><span class="script">Dinner</span><small>Grilled Chicken</small></div>
<div class="tile abs" style="left:777px;top:1858px;background:radial-gradient(circle,#f3ece0,#d8c7a8 60%,#b08d5a)" role="img" aria-label="Creamy pasta dish"></div>
<div class="tile abs" style="left:597px;top:2041px;background:radial-gradient(circle,#e6d3a0,#c9722e 55%,#5a3a22)" role="img" aria-label="Toasted wrap"></div>
<div class="tile dish-card abs" style="left:777px;top:2041px"><div class="dot"></div><span class="script">Lunch</span><small>Garden Salad</small></div>
<div class="tile dish-card abs" style="left:597px;top:2224px"><div class="dot"></div><span class="script">Dinner</span><small>Stone Pizza</small></div>
<div class="tile abs" style="left:777px;top:2224px;background:radial-gradient(circle,#dfe8c8,#7aa84a 55%,#c8402a)" role="img" aria-label="Fresh salad with tomatoes"></div>
<div class="tile dish-card abs" style="left:237px;top:2407px"><div class="dot"></div><span class="script">Lunch</span><small>Veggie Wrap</small></div>
<div class="tile abs" style="left:417px;top:2407px;background:radial-gradient(circle,#f3dca0,#e0b060 55%,#f4f0e6)" role="img" aria-label="Bowl of hummus"></div>
<div class="tile abs" style="left:597px;top:2407px;background:radial-gradient(circle,#e7e1d0,#b7a37a 55%,#4a3a2a)" role="img" aria-label="Flatbread with dips"></div>
<div class="tile abs" style="left:777px;top:2407px;background:radial-gradient(circle,#f2e6c6,#d49a4a 55%,#3a2a1e)" role="img" aria-label="Pizza slice"></div>

<section class="events abs" role="img" aria-label="Dark table with herbs and vegetables"></section>
<div class="events-title abs"><span class="script">Event</span> <span class="and script">and</span><span class="wide">Delivery</span></div>
<div class="events-text abs">
  <p>A special event requires a unique experience. Lanternhill comes to you with our signature dishes, full service and professionals in the planning of the menu. From a simple platter to a full spread, we bring the table to your home or venue.</p>
  <p>Hungry but no time to cook? Order online and we deliver hot and fresh to your door, with our full menu, drinks and desserts, ready whenever you are.</p>
</div>
<div class="events-photo abs" role="img" aria-label="Delivery bag and boxed pizza"></div>

<div class="offer abs" style="left:229px"><h3>Delivery</h3><p>Lanternhill delivers directly where you are, within our coverage area, with the same care found in our restaurant.</p></div>
<div class="offer-photo abs" role="img" aria-label="Overhead view of a shared platter"></div>
<div class="offer abs" style="left:688px;width:270px"><h3>Catering</h3><p>Let us cater your next dinner, birthday party or private event and bring a Mediterranean table to your home or venue.</p></div>

<div class="res-title abs"><span class="script">Reservation</span><span class="wide">Booking Table</span></div>
<section class="res-band abs"></section>
<div class="field abs" style="left:208px;width:240px">
  <svg width="18" height="18" viewBox="0 0 18 18"><rect x="1.5" y="3" width="15" height="13" fill="none" stroke="#fff" stroke-width="1.6"/><line x1="1.5" y1="7" x2="16.5" y2="7" stroke="#fff" stroke-width="1.6"/></svg>21/09/2024</div>
<div class="field abs" style="left:458px;width:115px">
  <svg width="18" height="18" viewBox="0 0 18 18"><circle cx="9" cy="9" r="7.5" fill="none" stroke="#fff" stroke-width="1.6"/><path d="M9 4.5V9l3 2" fill="none" stroke="#fff" stroke-width="1.6"/></svg>7:00 PM</div>
<div class="field abs" style="left:583px;width:178px">
  <svg width="18" height="18" viewBox="0 0 18 18"><circle cx="9" cy="6" r="3.5" fill="#fff"/><path d="M2 17c0-4 3-6 7-6s7 2 7 6z" fill="#fff"/></svg>02 People</div>
<div class="find abs">Find a Table</div>
<p class="res-note abs">Tables will only be held for 15 minutes past the reservation time. We appreciate your punctuality. Group bookings of six or more are welcome, please call ahead so we can prepare the perfect table for you and your guests.</p>

<footer class="footer abs"></footer>
<div class="foot-col abs" style="left:229px"><h4>Contact Us</h4><div>14 Ember Lane</div><div>Harbor City</div><div>(555) 014-2278</div><div>hello@lanternhill.test</div></div>
<div class="foot-col abs" style="left:396px"><h4>Opening Hours</h4><div>Monday – Thursday</div><div>11:00 – 22:00</div><div>Friday – Saturday</div><div>11:00 – 23:30</div><div>Sunday</div><div>12:00 – 21:00</div></div>
<div class="foot-col abs" style="left:604px"><h4>Follow Us</h4><div class="social"><span></span><span></span><span></span></div></div>
<div class="foot-col abs" style="left:760px;width:150px"><h4>Newsletter</h4><div class="input">Your name</div><div class="input">Your email</div></div>
<div class="foot-photo abs" role="img" aria-label="Plated dish on a red checked cloth"></div>

</body>
</html>
```